Need 5 pages of a marketing website designed

Need a simple site about a "mountain-town" digital marketing company designed around these topics. (UNCODED)
The homepage can mention these topics
- Website Creation / Management (New or Existing Websites & Hosting)
- Zentrik Search Marketing (Get Found in Zentrik Organic!)
- Social Media Marketing (Paid & Free Versions)
- Zentrik Shopfront Management (Get Found in Zentrik Atlas!)
- Video Content Creation & Marketing (Great for Clipvane & SM)
- Blog Content Creation & Marketing (Great for Zentrik & SM)
- Digital Marketing Consulting (Understand Best Marketing Options Based on Niche)
- Small Business Services (Phone Tracking Software / ROI Consulting / SOP Development)
And 1 service page created around 1 of the topics mentioned above (Ex - Social Media Marketing services), which I can duplicate for the other service pages
Please create these pages also
> Contact Us
> About Us
> Testimonials
Must be themed around Mountain Towns / ski resorts
I'm open to white / black / minor blues or orange for important areas
Can use Ipsum content for the text, just please create the headings etc
Lmk if you have any questions please

```html
<!DOCTYPE html>
<html lang="en">
<head>
<meta charset="utf-8">
<title>Alder Peak Marketing</title>
<link href="https://fonts.googleapis.com/css2?family=League+Spartan:wght@600;700;800&family=Roboto:wght@400;500;700&display=swap" rel="stylesheet">
<style>
:root{
  --blue:#1a6fb3;
  --blue-dark:#0f4f86;
  --orange:#f57f0c;
  --ink:#111;
  --text:#555;
  --contact-bg:#deedf4;
  --field:#eaf3f7;
  --peach:#fde4c8;
}
*{box-sizing:border-box;margin:0;padding:0}
html,body{width:1200px;height:3243px;overflow:hidden;background:#fff}
body{font-family:"Roboto",sans-serif;color:var(--text)}
.page{position:relative;width:1200px;height:3243px;overflow:hidden}
.abs{position:absolute}
.display{font-family:"League Spartan",sans-serif;font-weight:800;color:var(--ink);letter-spacing:.5px}
.btn{position:absolute;display:flex;align-items:center;justify-content:center;background:var(--orange);color:#fff;font-family:"League Spartan",sans-serif;font-weight:700;font-size:14px;letter-spacing:.3px;text-transform:uppercase}
.btn-outline{position:absolute;display:flex;align-items:center;justify-content:center;border:1.5px solid var(--blue);color:var(--blue);font-family:"Roboto",sans-serif;font-weight:700;font-size:13px;background:#fff}
.circle-btn{position:absolute;border-radius:50%;background:#fff;box-shadow:0 3px 10px rgba(0,0,0,.15);display:flex;align-items:center;justify-content:center}

.hero{position:absolute;left:0;top:0;width:1200px;height:585px;background:linear-gradient(180deg,#f7f8f9 0%,#e9ecee 30%,#b9c1c6 62%,#8c979e 100%)}
.brand{position:absolute;display:flex;align-items:center;gap:10px;font-family:"Roboto",sans-serif;font-weight:700;white-space:nowrap}
.brand .mark{width:14px;height:14px}
.top-contact{position:absolute;top:13px;display:flex;align-items:center;gap:10px;font-size:12px;color:#222}
.top-contact .ico{width:30px;height:30px;border-radius:50%;background:var(--orange);display:flex;align-items:center;justify-content:center}
.nav{position:absolute;top:58px;left:537px;display:flex;gap:29px;font-family:"Roboto",sans-serif;font-weight:500;font-size:13px;color:#1d1d1d}
.nav .active{color:var(--blue)}
.hero-kicker{position:absolute;left:150px;top:222px;font-family:"League Spartan",sans-serif;font-weight:800;font-size:25px;color:var(--blue)}
.hero-title{position:absolute;left:150px;top:256px;font-size:45px;line-height:45px}
.dots span{position:absolute;left:1040px;width:11px;height:11px;border-radius:50%;border:1.5px solid var(--blue)}

.about-title{position:absolute;left:657px;top:697px;font-size:42px}
.about-copy{position:absolute;left:657px;width:395px;font-size:12px;line-height:20px;color:#555}

.services{position:absolute;left:0;top:1168px;width:1200px;height:721px;background:linear-gradient(180deg,#f3f4f5 0%,#eceeef 45%,#c9cdd0 80%,#b7bcc0 100%)}
.section-title{position:absolute;left:0;width:1200px;text-align:center;font-size:42px}
.card{position:absolute;top:1338px;width:270px;height:365px;background:#fff;border-radius:0 0 14px 14px;box-shadow:0 6px 18px rgba(0,0,0,.08);overflow:hidden}
.card .photo{width:270px;height:173px}
.card h3{font-family:"Roboto",sans-serif;font-weight:700;font-size:15px;color:#111;text-align:center;margin-top:22px;line-height:18px;padding:0 18px}
.card p{font-size:10.5px;line-height:16px;color:#666;text-align:center;padding:0 20px;margin-top:10px}
.card .btn-outline{left:80px;top:310px;width:110px;height:36px}

.quote-card{position:absolute;top:2068px;width:432px;height:246px;background:#fff;border-radius:10px;box-shadow:0 6px 24px rgba(0,0,0,.08)}
.quote-card .avatar{position:absolute;left:48px;top:39px;width:80px;height:80px;border-radius:50%}
.quote-card .name{position:absolute;left:145px;top:46px;font-family:"League Spartan",sans-serif;font-weight:700;font-size:17px;color:#111}
.quote-card .role{position:absolute;left:145px;top:72px;font-size:13px;color:#666}
.quote-card .stars{position:absolute;left:145px;top:92px}
.quote-card .marks{position:absolute;left:343px;top:30px;font-family:"League Spartan",sans-serif;font-weight:800;font-size:120px;line-height:120px;color:#e8e8e8}
.quote-card p{position:absolute;left:48px;top:143px;width:358px;font-size:12px;line-height:20px;color:#666}

.contact{position:absolute;left:0;top:2411px;width:1200px;height:540px;background:var(--contact-bg)}
.field{position:absolute;background:var(--field);border:1px solid #d5e3ea;font-size:12px;color:#777;padding:14px 18px}

.footer{position:absolute;left:0;top:2950px;width:1200px;height:293px;background:linear-gradient(180deg,#1a1c1f 0%,#0d0e10 100%);color:#fff}
.foot-head{position:absolute;font-family:"League Spartan",sans-serif;font-weight:700;font-size:16px;letter-spacing:.3px;color:#fff;white-space:nowrap}
.foot-links{position:absolute;left:403px;font-size:12px;line-height:20px;font-weight:500;color:#fff}
.foot-item{position:absolute;left:617px;font-size:12px;line-height:20px;font-weight:500;color:#fff;white-space:nowrap}
.social{position:absolute;top:3103px;width:28px;height:28px;border-radius:50%;background:var(--orange)}
</style>
</head>
<body>
<div class="page">

  <section class="hero" role="img" aria-label="Snowy mountain range backdrop in soft greys"></section>

  <div class="brand" style="left:150px;top:52px;font-size:20px;color:var(--blue-dark)">
    <span class="mark" style="background:var(--blue-dark)"></span>Alder Peak Marketing
  </div>

  <div class="top-contact" style="left:697px">
    <span class="ico"><svg width="14" height="14" viewBox="0 0 24 24"><path fill="#fff" d="M6.6 10.8a15.1 15.1 0 006.6 6.6l2.2-2.2c.3-.3.7-.4 1-.2 1.1.4 2.3.6 3.6.6.6 0 1 .4 1 1V20c0 .6-.4 1-1 1A17 17 0 013 4c0-.6.4-1 1-1h3.5c.6 0 1 .4 1 1 0 1.3.2 2.5.6 3.6.1.3 0 .7-.2 1z"/></svg></span>555 014 2290
  </div>
  <div class="top-contact" style="left:851px">
    <span class="ico"><svg width="14" height="12" viewBox="0 0 24 18"><rect x="1" y="1" width="22" height="16" rx="2" fill="none" stroke="#fff" stroke-width="2"/><path d="M1 2l11 8 11-8" fill="none" stroke="#fff" stroke-width="2"/></svg></span>hello@peakridgemedia.com
  </div>

  <nav class="nav">
    <span class="active">HOME</span><span>ABOUT US</span><span>TESTIMONIALS</span><span style="margin-left:4px">BLOG</span>
  </nav>
  <div class="btn" style="left:890px;top:47px;width:110px;height:36px;font-family:'Roboto',sans-serif;font-weight:500;font-size:13px">CONTACT US</div>
  <svg class="abs" style="left:1028px;top:52px" width="24" height="24" viewBox="0 0 24 24"><circle cx="10" cy="10" r="7.5" fill="none" stroke="var(--blue-dark)" stroke-width="2.2"/><path d="M15.5 15.5L22 22" stroke="var(--blue-dark)" stroke-width="2.4" stroke-linecap="round"/></svg>

  <div class="hero-kicker">WELCOME TO</div>
  <h1 class="hero-title display">ALDER PEAK<br>MARKETING</h1>
  <div class="btn" style="left:150px;top:369px;width:131px;height:37px">CONTACT NOW</div>

  <svg class="abs" style="left:529px;top:94px" width="500" height="456" viewBox="0 0 500 456">
    <path d="M60 110c10-40 60-40 80-20 40 10 50 60 30 90-20 30-70 30-95 10C55 175 52 140 60 110z" fill="var(--blue)"/>
    <path d="M300 60c40-10 90 10 110 50 15 30-10 60-40 50-40-15-90-40-70-100z" fill="var(--blue)"/>
    <path d="M100 360c30-30 90-20 110 10 15 25-10 55-50 55-45 0-85-30-60-65z" fill="var(--blue)"/>
    <path d="M330 300c40-10 100 20 80 60-15 25-60 25-80 5-20-20-25-55 0-65z" fill="var(--blue)"/>
    <path role="img" aria-label="Photo of a team working at laptops in a bright office" fill="#9aa6ad" d="M150 40c40-45 120-50 160-10 25 30 20 60 60 70 45 10 90 30 110 80 20 55-10 110-60 120-40 8-60 40-70 80-12 45-70 60-120 45-45-13-60-50-100-55-50-7-100-30-110-85-8-45 25-75 50-100 30-30 45-100 80-145z"/>
    <path d="M60 110C120 20 260-10 330 30" fill="none" stroke="#fff" stroke-width="1.5" opacity=".8"/>
  </svg>

  <div class="dots">
    <span style="top:280px;background:var(--blue)"></span>
    <span style="top:303px"></span>
    <span style="top:327px"></span>
  </div>

  <div class="circle-btn" style="left:604px;top:567px;width:44px;height:44px">
    <svg width="16" height="18" viewBox="0 0 16 18"><path d="M8 1v15M2 10l6 6 6-6" fill="none" stroke="var(--blue)" stroke-width="2.2" stroke-linecap="round"/></svg>
  </div>

  <svg class="abs" style="left:79px;top:678px" width="530" height="440" viewBox="0 0 530 440">
    <circle cx="145" cy="148" r="145" fill="var(--peach)"/>
    <path role="img" aria-label="Photo of two colleagues smiling over a laptop and reports" fill="#b7a99c" d="M250 0c90-5 180 40 215 130 35 90 15 200-60 260-70 55-180 60-260 20C70 370 50 300 70 240c15-50 20-90 40-140C135 40 180 4 250 0z"/>
  </svg>

  <h2 class="about-title display">ABOUT US</h2>
  <p class="about-copy" style="top:767px">Lorem ipsum dolor sit amet, consectetur adipiscing elit, sed do enimmod tempor incididunt ut labore et dolore magna aliqua. Quis ipsum disse eu ultrices gravida. Risus commodo viverra maecenas Fusce at lacinia sedmauris.</p>
  <p class="about-copy" style="top:861px">accumsan lacus vel facilisis. Fusce at lacinia mauris. Fusce eleifend purus risus, sed lacinia nisl tempus sit amet. Morbi hendrerit ex non fau ipsum feugiat, sit amet pretium est condimentum.Fusce eleifend purus risus.Lorem ipsum dolor sit amet.consectetur adipiscing elit. Mauris cibus elementum dapibus.Nunc posuere facilisis lacus sit amet ametlis. Mauris vel elit tincidunt, volutpat mi at, lacinia elit. Mauris vel elit tincidunt, volutpat mi at, lacinia elit.</p>
  <div class="btn" style="left:657px;top:1044px;width:110px;height:36px">READ MORE</div>

  <section class="services" role="img" aria-label="Faded mountain ridges background"></section>
  <h2 class="section-title display" style="top:1242px">OUR SERVICES</h2>
  <div class="circle-btn" style="left:968px;top:1270px;width:38px;height:38px">
    <svg width="16" height="14" viewBox="0 0 16 14"><path d="M15 7H2M7 1L1 7l6 6" fill="none" stroke="var(--blue-dark)" stroke-width="2" stroke-linecap="round"/></svg>
  </div>
  <div class="circle-btn" style="left:1012px;top:1270px;width:38px;height:38px">
    <svg width="16" height="14" viewBox="0 0 16 14"><path d="M1 7h13M9 1l6 6-6 6" fill="none" stroke="#9bb" stroke-width="2" stroke-linecap="round"/></svg>
  </div>

  <div class="abs" style="left:62px;top:1448px;width:150px;height:200px;border-radius:50%;background:#7fb6dd;opacity:.75"></div>
  <div class="abs" style="left:920px;top:1572px;width:185px;height:198px;border-radius:48% 52% 45% 55%;background:#f2bd84;opacity:.7"></div>

  <article class="card" style="left:150px">
    <div class="photo" role="img" aria-label="Photo of a developer at a laptop with code icons" style="background:linear-gradient(135deg,#9fb6c9,#2d5a86)"></div>
    <h3>Website Creation /<br>Management</h3>
    <p>Lorem ipsum dolor sit amet, consectetur adipiscing elit, sed do eiusmod tempor adunt ut labore et dolore magna aliqua.</p>
    <div class="btn-outline">READ MORE</div>
  </article>
  <article class="card" style="left:461px">
    <div class="photo" role="img" aria-label="Photo of hands typing a search on a laptop" style="background:linear-gradient(135deg,#6a7f96,#c9c3b8)"></div>
    <h3>Zentrik Search Marketing</h3>
    <p>Lorem ipsum dolor sit amet, consectetur adipiscing elit, sed do eiusmod tempor adunt ut labore et dolore magna aliqua.</p>
    <div class="btn-outline">READ MORE</div>
  </article>
  <article class="card" style="left:770px">
    <div class="photo" role="img" aria-label="Photo of a laptop showing a blog page" style="background:linear-gradient(135deg,#b89a8c,#f0b52a)"></div>
    <h3>Blog Content Creation &amp;<br>Marketing</h3>
    <p>Lorem ipsum dolor sit amet, consectetur adipiscing elit, sed do eiusmod tempor adunt ut labore et dolore magna aliqua.</p>
    <div class="btn-outline">READ MORE</div>
  </article>

  <div class="btn" style="left:520px;top:1773px;width:160px;height:37px">VIEW ALL SERVICES</div>

  <h2 class="section-title display" style="top:1972px">WHAT OUR CLIENT SAYS</h2>

  <div class="quote-card" style="left:151px">
    <div class="avatar" role="img" aria-label="Client portrait" style="background:#6d6a66"></div>
    <div class="name">MARA ELLISON</div>
    <div class="role">Alpine Stride Physio</div>
    <svg class="stars" width="100" height="18" viewBox="0 0 100 18"><g fill="#f5a300"><path id="st" d="M9 1l2.4 5.3 5.7.6-4.3 3.8 1.3 5.6L9 13.4 3.9 16.3l1.3-5.6L.9 6.9l5.7-.6z"/><use href="#st" x="20"/><use href="#st" x="40"/><use href="#st" x="60"/><use href="#st" x="80"/></g></svg>
    <div class="marks">”</div>
    <p>Lorem ipsum dolor sit amet, consectetur adipiscing elit, sed do eiusmod tempor incididunt ut labore et dolore magna aliqua. Quis ipsum suspendisse ultrices gravida.</p>
  </div>
  <div class="quote-card" style="left:618px">
    <div class="avatar" role="img" aria-label="Client portrait" style="background:#c7ccd3"></div>
    <div class="name">MARA ELLISON</div>
    <div class="role">Alpine Stride Physio</div>
    <svg class="stars" width="100" height="18" viewBox="0 0 100 18"><g fill="#f5a300"><use href="#st"/><use href="#st" x="20"/><use href="#st" x="40"/><use href="#st" x="60"/><use href="#st" x="80"/></g></svg>
    <div class="marks">”</div>
    <p>Lorem ipsum dolor sit amet, consectetur adipiscing elit, sed do eiusmod tempor incididunt ut labore et dolore magna aliqua. Quis ipsum suspendisse ultrices gravida.</p>
  </div>

  <div class="circle-btn" style="left:124px;top:2178px;width:44px;height:44px">
    <svg width="18" height="14" viewBox="0 0 18 14"><path d="M17 7H2M7 1L1 7l6 6" fill="none" stroke="#9bb0c0" stroke-width="2" stroke-linecap="round"/></svg>
  </div>
  <div class="circle-btn" style="left:1033px;top:2178px;width:44px;height:44px">
    <svg width="18" height="14" viewBox="0 0 18 14"><path d="M1 7h15M11 1l6 6-6 6" fill="none" stroke="var(--blue-dark)" stroke-width="2.2" stroke-linecap="round"/></svg>
  </div>

  <section class="contact"></section>
  <h2 class="display abs" style="left:150px;top:2495px;font-size:42px">CONTACT NOW</h2>
  <div class="field" style="left:150px;top:2572px;width:212px;height:44px">Name</div>
  <div class="field" style="left:370px;top:2572px;width:213px;height:44px">E-mail</div>
  <div class="field" style="left:150px;top:2626px;width:212px;height:44px">Telephone</div>
  <div class="field" style="left:370px;top:2626px;width:213px;height:44px">Company</div>
  <div class="field" style="left:150px;top:2682px;width:433px;height:118px">Message</div>
  <div class="btn" style="left:150px;top:2820px;width:111px;height:37px">SUBMIT</div>

  <svg class="abs" style="left:633px;top:2470px" width="430" height="422" viewBox="0 0 430 422">
    <ellipse cx="350" cy="340" rx="60" ry="70" fill="#8fc6e2"/>
    <path role="img" aria-label="Photo of a woman on the phone working at a laptop" fill="#8a6a4c" d="M180 2c90-10 170 30 215 100 40 65 30 150-20 210-50 60-130 100-220 105C80 422 20 380 5 310-10 240 10 180 30 130 55 60 100 10 180 2z"/>
  </svg>

  <footer class="footer" role="img" aria-label="Dark mountain silhouette backdrop"></footer>
  <div class="brand" style="left:150px;top:3050px;font-size:20px;color:#fff">
    <span class="mark" style="background:#fff"></span>Alder Peak Marketing
  </div>
  <span class="social" style="left:148px"></span>
  <span class="social" style="left:182px"></span>
  <span class="social" style="left:216px"></span>
  <span class="social" style="left:250px"></span>

  <div class="foot-head" style="left:403px;top:3006px">QUICK LINK</div>
  <div class="foot-links" style="top:3030px">Home<br>About Us<br>Services<br>Blog<br>Testimonials<br>Contact</div>

  <div class="foot-head" style="left:582px;top:3006px">CONTACT NOW</div>
  <svg class="abs" style="left:583px;top:3034px" width="16" height="16" viewBox="0 0 24 24"><path fill="var(--orange)" d="M6.6 10.8a15.1 15.1 0 006.6 6.6l2.2-2.2c.3-.3.7-.4 1-.2 1.1.4 2.3.6 3.6.6.6 0 1 .4 1 1V20c0 .6-.4 1-1 1A17 17 0 013 4c0-.6.4-1 1-1h3.5c.6 0 1 .4 1 1 0 1.3.2 2.5.6 3.6.1.3 0 .7-.2 1z"/></svg>
  <div class="foot-item" style="top:3030px">Contact Number<br>+1 555 018 4420</div>
  <svg class="abs" style="left:582px;top:3081px" width="18" height="13" viewBox="0 0 24 18"><rect x="1" y="1" width="22" height="16" rx="2" fill="var(--orange)"/><path d="M1 2l11 8 11-8" fill="none" stroke="#111" stroke-width="1.6"/></svg>
  <div class="foot-item" style="top:3075px">Email Address<br>info@summitlane.com</div>
  <svg class="abs" style="left:584px;top:3122px" width="14" height="18" viewBox="0 0 14 18"><path fill="var(--orange)" d="M7 0a7 7 0 00-7 7c0 5 7 11 7 11s7-6 7-11a7 7 0 00-7-7zm0 9.5A2.5 2.5 0 117 4.5a2.5 2.5 0 010 5z"/></svg>
  <div class="foot-item" style="top:3120px">Office Location<br>12 Ridgeway Rd, Pine Hollow</div>

  <div class="foot-head" style="left:782px;top:3006px">SUBSCRIBE TO OUR NEWSLETTER</div>
  <div class="abs" style="left:782px;top:3030px;width:161px;height:36px;border:1px solid #fff;font-size:11px;color:#ddd;padding:11px 14px">Enter your email</div>
  <div class="abs" style="left:943px;top:3030px;width:108px;height:36px;background:#fff;color:#111;font-family:'Roboto',sans-serif;font-weight:700;font-size:11px;display:flex;align-items:center;justify-content:center">SUBSCRIBE</div>

  <div class="abs" style="left:176px;top:3204px;width:900px;height:1px;background:#5a5d60"></div>
  <div class="abs" style="left:0;top:3218px;width:1200px;text-align:center;font-size:10px;color:#ddd">Copyright © 2024 Alder Peak Marketing.All Rights Reserved.</div>

</div>
</body>
</html>
```